Haunted Attraction Expert Website Design

A complete professional looking web site with 6 total pages.
Includes calendar and email form.
Needs to be word press and mobile user friendly.
Please use photos as labeled for the pages they will be presented on.
Company logo should alternate left and right sides of the page.
See attached layout for directions

Target Market(s)

Professionals, Haunted Attraction Owners/Operators

Industry/Entity Type

It Professional

Coding

Coded - Design and coding required

Number of Pages Required

5+ page

Font styles to use
Sans Serif

Colors

Designer to choose colors to be used in the design.

Requirements
Must have
• Our company logo on each page and photos supplied by me assigned to specific pages.
• Calendar
• Contact US Email Submission Form

```html
<!DOCTYPE html>
<html lang="en">
<head>
<meta charset="utf-8">
<title>Expert Witnesses – Nightfall Attraction Advisors</title>
<link href="https://fonts.googleapis.com/css2?family=Exo+2:ital,wght@0,400;0,600;0,700;1,400&family=Open+Sans:wght@400;600&display=swap" rel="stylesheet">
<style>
  :root {
    --orange: #f7931e;
    --black: #050505;
    --header-top: #1c1c1c;
    --page-bg: #f9f9f9;
    --card-bg: #f1f1f1;
    --ink: #111111;
    --muted: #555555;
    --soft: #7a7a7a;
    --rule: #d6d6d6;
    --white: #ffffff;
  }
  * { box-sizing: border-box; margin: 0; padding: 0; }
  html, body { width: 802px; height: 1200px; overflow: hidden; background: var(--white); }
  body { font-family: "Open Sans", sans-serif; color: var(--ink); }
  .page { position: relative; width: 802px; height: 1200px; overflow: hidden; }

  .site-header {
    position: absolute; left: 0; top: 0; width: 802px; height: 39px;
    background: linear-gradient(var(--header-top), var(--black));
    z-index: 2;
  }
  .brand {
    position: absolute; left: 134px; top: 0; width: 130px; height: 92px;
    background: #1a1d22;
    clip-path: polygon(0 0, 100% 0, 100% 88%, 50% 100%, 0 88%);
    display: flex; flex-direction: column; align-items: center; justify-content: center;
    gap: 6px; z-index: 3;
  }
  .brand-mark { width: 14px; height: 14px; border-radius: 50%; background: var(--orange); }
  .brand-name {
    font-family: "Exo 2", sans-serif; font-weight: 600; font-size: 11px;
    color: var(--orange); text-align: center; line-height: 1.2; letter-spacing: .3px;
  }
  .main-nav { position: absolute; right: 133px; top: 0; height: 39px; display: flex; }
  .main-nav a {
    display: flex; align-items: center; height: 39px; padding: 0 7px;
    font-size: 6.8px; font-weight: 600; color: var(--white); text-decoration: none;
    text-transform: uppercase; letter-spacing: .2px;
  }
  .main-nav a.is-active { background: var(--orange); padding: 0 7px; }

  .content { position: absolute; left: 0; top: 39px; width: 802px; height: 695px; background: var(--page-bg); }
  .wrap { position: absolute; left: 134px; width: 535px; }
  .page-title { top: 64px; font-family: "Exo 2", sans-serif; font-weight: 600; font-size: 17px; }
  .intro { top: 94px; font-size: 7.6px; line-height: 12px; color: #333; }
  .hero-photo {
    top: 133px; height: 265px;
    background: radial-gradient(ellipse at 35% 35%, #6b625a 0%, #3b342e 45%, #17130f 100%);
  }
  .contact-lead { top: 410px; font-family: "Exo 2", sans-serif; font-weight: 600; font-size: 13.6px; line-height: 17px; }

  .experts { top: 456px; list-style: none; }
  .expert { margin-bottom: 9px; }
  .expert-line {
    height: 35px; background: var(--card-bg); padding-left: 8px;
    display: flex; align-items: center;
    font-family: "Exo 2", sans-serif; font-size: 11.4px; color: var(--soft);
  }
  .expert-cv {
    display: block; height: 12px; background: var(--orange); padding-left: 8px;
    font-size: 6.2px; line-height: 12px; color: var(--white); text-decoration: none;
  }

  .quote {
    position: absolute; left: 134px; top: 756px; width: 535px; height: 74px;
    border-top: 1px solid var(--rule); border-bottom: 1px solid var(--rule);
    text-align: center; padding-top: 10px;
  }
  .quote p { font-family: "Exo 2", sans-serif; font-style: italic; font-size: 17.5px; line-height: 18px; color: var(--soft); }
  .quote cite { display: block; font-style: normal; font-size: 11.5px; margin-top: 3px; color: var(--ink); }

  .contact {
    position: absolute; left: 0; top: 853px; width: 802px; height: 347px;
    background: radial-gradient(ellipse at 50% 40%, #3a3036 0%, #221b20 50%, #0e0b0d 100%);
  }
  .contact-title {
    position: absolute; left: 0; width: 802px; top: 16px; text-align: center;
    font-family: "Exo 2", sans-serif; font-weight: 600; font-size: 23px; letter-spacing: 1.5px; color: var(--white);
  }
  .contact-form { position: absolute; left: 229px; top: 57px; width: 346px; }
  .field {
    display: block; width: 345px; height: 29px; margin-bottom: 6px;
    background: var(--white); padding: 0 9px; font-size: 7.4px; color: #444;
    display: flex; align-items: center;
  }
  .field-message { height: 69px; align-items: flex-start; padding-top: 12px; margin-bottom: 10px; }
  .submit {
    width: 346px; height: 28px; background: var(--orange); border-radius: 3px;
    color: var(--white); font-size: 7.4px; font-weight: 600; text-align: center; line-height: 28px;
  }
  .contact-info {
    position: absolute; left: 0; width: 802px; top: 285px; text-align: center;
    color: var(--white); font-size: 9.2px; line-height: 14px;
  }
  .contact-info svg { display: block; margin: 0 auto 4px; }
</style>
</head>
<body>
<div class="page">
  <header class="site-header">
    <div class="brand">
      <span class="brand-mark"></span>
      <span class="brand-name">NIGHTFALL<br>ATTRACTION ADVISORS</span>
    </div>
    <nav class="main-nav">
      <a href="#">Home</a>
      <a href="#">About</a>
      <a href="#">Consulting</a>
      <a href="#" class="is-active">Expert Witnesses</a>
      <a href="#">Upcoming Events</a>
      <a href="#">Contact Us</a>
    </nav>
  </header>

  <main class="content">
    <h1 class="wrap page-title">Expert Witnesses</h1>
    <p class="wrap intro">Nightfall Attraction Advisors provide forensic litigation consulting and expert witness services for lawsuits and legal cases involving cata-strophic injuries, fatalities, personal injuries, and workplace safety.</p>
    <div class="wrap hero-photo" role="img" aria-label="Costumed haunted attraction actor typing at an antique typewriter in a dim, cluttered room"></div>
    <h2 class="wrap contact-lead">To discuss litigation consulting or expert witness services contact one of our Industry Experts below:</h2>
    <ul class="wrap experts">
      <li class="expert"><div class="expert-line">Warren Holbeck email wholbeck@mailbox.example or call 555-204-1187</div><a class="expert-cv" href="#">Click here to access CV (from Lexpro link)</a></li>
      <li class="expert"><div class="expert-line">Dana Whitcombe email dana@darkhollowtours.example or call 555-318-4462</div><a class="expert-cv" href="#">Click here to access CV</a></li>
      <li class="expert"><div class="expert-line">Gerald Ashworth email gashworth@netmail.example or call 555-627-0935</div><a class="expert-cv" href="#">Click here to access CV</a></li>
      <li class="expert"><div class="expert-line">Martin Crowley email martin@fogline.example&nbsp; or call 555-742-6190</div><a class="expert-cv" href="#">Click here to access CV</a></li>
    </ul>
  </main>

  <blockquote class="quote">
    <p>Happiness and personal fulfillment are the natural consequences<br>of doing the right thing.</p>
    <cite>Marcus Vell</cite>
  </blockquote>

  <section class="contact" role="img" aria-label="Group of costumed haunted attraction performers in dark makeup behind the contact form">
    <h2 class="contact-title">CONTACT US</h2>
    <form class="contact-form">
      <div class="field">Your Name</div>
      <div class="field">Your Email</div>
      <div class="field">Company Name</div>
      <div class="field field-message">Your Message</div>
      <div class="submit">SUBMIT NOW</div>
    </form>
    <div class="contact-info">
      <svg width="12" height="16" viewBox="0 0 12 16" aria-hidden="true"><path d="M6 0C2.7 0 0 2.6 0 5.9 0 10.3 6 16 6 16s6-5.7 6-10.1C12 2.6 9.3 0 6 0zm0 8.2a2.3 2.3 0 1 1 0-4.6 2.3 2.3 0 0 1 0 4.6z" fill="#ffffff"/></svg>
      Lorem ipsum dolor sit amet #13-29 Duis autem ve dolor, USA 118535<br>
      0800 123 456 790 - 1200 234 5045&nbsp;&nbsp;&nbsp; wholbeck@mailbox.example
    </div>
  </section>
</div>
</body>
</html>
```